Quillmere Business Card

I have a current card that I like it just needs a couple little changes to make it perfect. I would like the font size bigger so it could be easily read by older customers.

Business

```html
<!DOCTYPE html>
<html lang="en">
<head>
<meta charset="utf-8">
<title>Quillmere Business Card</title>
<link rel="stylesheet" href="https://fonts.googleapis.com/css2?family=Quicksand:wght@500;600;700&display=swap">
<style>
  :root {
    --card-bg: #fffff2;
    --ink: #2b2219;
  }
  html, body {
    margin: 0;
    padding: 0;
    overflow: hidden;
    background: var(--card-bg);
  }
  .card {
    position: relative;
    width: 1200px;
    height: 702px;
    background: var(--card-bg);
    color: var(--ink);
    font-family: "Quicksand", sans-serif;
    overflow: hidden;
  }
  .services {
    position: absolute;
    top: 39px;
    left: 0;
    width: 100%;
    margin: 0;
    text-align: center;
    font-weight: 500;
    font-size: 42px;
    line-height: 49px;
    word-spacing: 8px;
    transform: scaleX(0.93);
    transform-origin: 50% 0;
  }
  .hours-title {
    position: absolute;
    top: 471px;
    left: 0;
    width: 1234px;
    margin: 0;
    text-align: center;
    font-weight: 600;
    font-size: 56px;
    line-height: 60px;
    letter-spacing: -1px;
    transform: scaleX(0.83);
    transform-origin: 50% 0;
  }
  .hours-cell {
    position: absolute;
    font-weight: 600;
    font-size: 56px;
    line-height: 60px;
    letter-spacing: -1px;
    white-space: nowrap;
    transform: scaleX(0.83);
    transform-origin: 0 0;
  }
  .day-mon  { top: 529px; left: 66px; }
  .time-mon { top: 529px; left: 312px; }
  .day-thu  { top: 529px; left: 689px; }
  .time-thu { top: 529px; left: 816px; }
  .day-fri  { top: 588px; left: 158px; }
  .time-fri { top: 588px; left: 312px; }
  .day-sat  { top: 588px; left: 710px; }
  .time-sat { top: 588px; left: 816px; }
</style>
</head>
<body>
  <main class="card">
    <p class="services">
      Servicing all makes &amp; models of boats,<br>
      snowmobiles, motorcycles and ATV’s.<br>
      Custom welding available for aluminum and steel.
    </p>

    <h2 class="hours-title">Hours:</h2>

    <span class="hours-cell day-mon">Mon - Wed</span>
    <span class="hours-cell time-mon">9 am - 5:30 pm</span>
    <span class="hours-cell day-thu">Thurs</span>
    <span class="hours-cell time-thu">9 am&nbsp; - 7:00 pm</span>
    <span class="hours-cell day-fri">Fri</span>
    <span class="hours-cell time-fri">9 am - 5:30 pm</span>
    <span class="hours-cell day-sat">Sat</span>
    <span class="hours-cell time-sat">9 am&nbsp; - 3:30 pm</span>
  </main>
</body>
</html>
```